Business Recognition Design

We need a design for a recognition to be given to business leaders in our community.
The recognition shall be made on a brass plaque on wood panel background (picture attached, please use it as a background), and all drawing must be in vectors and only one color (black).
It should also have a logo on the top and signature on the right bottom.
The text is enclosed in DOC file.
Updates

Reason: just to be able to find the best solution

Reason: None of the suggestion is good enough. Logo in general is too big in comparison with the rest of the plate.

Industry/Entity Type

Business

Requirements
Must have
• - standard Windows font (or possibility to install the same font on Windows), as the name on the recognition shall be printed in the same font
Nice to have
• - some graphic element (in curves) representing achievements in business
- should look great :)

```html
<!DOCTYPE html>
<html lang="de">
<head>
<meta charset="utf-8">
<title>Auszeichnung – KapitalWerk</title>
<link rel="stylesheet" href="https://fonts.googleapis.com/css2?family=Arimo:wght@400;700&display=swap">
<style>
  :root {
    --wood-dark: #5a2f16;
    --wood-mid: #7d4a26;
    --wood-light: #94603a;
    --brass-deep: #b48a2a;
    --brass-mid: #d8b547;
    --brass-light: #f3dc82;
    --screw-rim: #7a5a1c;
    --screw-face: #e6c865;
    --ink: #0d0b06;
  }
  * { margin: 0; padding: 0; box-sizing: border-box; }
  html, body { width: 1200px; height: 931px; overflow: hidden; background: #ffffff; }
  .award {
    position: relative;
    width: 1200px;
    height: 931px;
    font-family: "Arimo", Arial, sans-serif;
    color: var(--ink);
  }
  .wood-panel {
    position: absolute;
    inset: 0;
    border-radius: 8px;
    background:
      linear-gradient(90deg, rgba(0,0,0,0.18), rgba(255,255,255,0.04) 30%, rgba(0,0,0,0.10) 60%, rgba(255,255,255,0.05) 85%, rgba(0,0,0,0.2)),
      linear-gradient(180deg, var(--wood-light), var(--wood-mid) 45%, var(--wood-dark));
  }
  .brass-plate {
    position: absolute;
    left: 28px; top: 28px;
    width: 1142px; height: 872px;
    background:
      linear-gradient(135deg, var(--brass-deep) 0%, var(--brass-mid) 22%, var(--brass-light) 48%, var(--brass-mid) 70%, var(--brass-deep) 100%);
    box-shadow: 0 3px 6px rgba(0,0,0,0.45);
  }
  .screw {
    position: absolute;
    width: 28px; height: 28px;
    border-radius: 50%;
    background: radial-gradient(circle at 38% 35%, var(--brass-light), var(--screw-face) 45%, var(--screw-rim));
    box-shadow: 0 1px 2px rgba(0,0,0,0.5);
  }
  .screw.top-left { left: 75px; top: 75px; }
  .screw.top-right { left: 1097px; top: 75px; }
  .screw.bottom-left { left: 75px; top: 828px; }
  .screw.bottom-right { left: 1097px; top: 828px; }

  .line { position: absolute; left: 0; width: 1200px; text-align: center; white-space: nowrap; line-height: 1; }
  .brand-name { top: 190px; font-size: 80px; font-weight: 700; letter-spacing: -1px; }
  .brand-rule { position: absolute; left: 344px; top: 298px; width: 514px; height: 6px; background: var(--ink); }
  .award-title { top: 326px; font-size: 50px; font-weight: 700; }
  .award-reason { top: 397px; font-size: 44px; }
  .award-year { top: 462px; font-size: 52px; }
  .award-for { top: 543px; font-size: 28px; }
  .recipient { top: 600px; font-size: 44px; }
  .recipient strong { font-weight: 700; }
  .citation { font-size: 21px; }
  .citation.first { top: 695px; }
  .citation.second { top: 732px; }
  .place-date, .signatory { position: absolute; top: 808px; font-size: 22px; white-space: nowrap; line-height: 1; }
  .place-date { left: 203px; }
  .signatory { left: 786px; }
</style>
</head>
<body>
<main class="award">
  <div class="wood-panel" role="img" aria-label="Walnut wood panel backing"></div>
  <section class="brass-plate" role="img" aria-label="Brushed brass plate"></section>
  <span class="screw top-left"></span>
  <span class="screw top-right"></span>
  <span class="screw bottom-left"></span>
  <span class="screw bottom-right"></span>

  <div class="line brand-name">KapitalWerk</div>
  <div class="brand-rule"></div>
  <h1 class="line award-title">AUSZEICHNUNG</h1>
  <p class="line award-reason">als herausragendster Unternehmer</p>
  <p class="line award-year">Deutschlands 2013</p>
  <p class="line award-for">für</p>
  <p class="line recipient">Herrn Dipl.-Kfm. <strong>Erik Beispiel</strong></p>
  <p class="line citation first">Unter der Leitung von Herr Dipl.-Kfm. Erik Beispiel hat sich die FIRMA GmbH im Jahr</p>
  <p class="line citation second">2013 unter den ersten 5% der größten deutschen Wirtschaftsunternehmen platziert.</p>
  <p class="place-date">Gilching, 20. Juni 2013</p>
  <p class="signatory">Helena Brandt</p>
</main>
</body>
</html>
```